Business Card Design for Miss Poppy's Soak Parlour

Name: Miss Poppy's Soak Parlour. Maker of bath bombs, bath salts.

Card details:

Donna Pickett
1.702.555.0143
Silver Hollow Nevada
dpickett47@mailpost.example

"Bath bombs, bath salts and more..."

A picture of an old-fashioned bathtub (with claw feet) filled with bath bombs.

Colors include: Lavender, Pink, Turquois, Light Blue. Can you make the overall design look old fashioned.

```html
<!DOCTYPE html>
<html lang="en">
<head>
<meta charset="utf-8">
<title>Miss Poppy's Soak Parlour — Business Card</title>
<link rel="stylesheet" href="https://fonts.googleapis.com/css2?family=Jost:wght@300&family=Open+Sans:wght@400;700&display=swap">
<style>
  :root {
    --backdrop: #3a3430;
    --card: #0d0d0d;
    --card-edge: #1c1c1c;
    --ink: #f2f2f2;
    --silver: #c9c9c9;
    --muted: #a8a8a8;
  }
  * { box-sizing: border-box; margin: 0; padding: 0; }
  html, body { width: 1200px; height: 900px; overflow: hidden; }
  body {
    background: var(--backdrop);
    position: relative;
    font-family: "Open Sans", sans-serif;
  }
  .card {
    position: absolute;
    top: 290px;
    width: 520px;
    height: 300px;
    background: radial-gradient(ellipse at 60% 40%, #161616, var(--card) 70%);
    border: 1px solid var(--card-edge);
    box-shadow: 0 14px 30px rgba(0,0,0,.45);
    overflow: hidden;
  }
  .card--front { left: 70px; }
  .card--back { left: 610px; }

  .brand {
    font-family: "Jost", sans-serif;
    font-weight: 300;
    text-transform: uppercase;
    line-height: 1.1;
    text-align: center;
    color: var(--ink);
  }
  .brand__name { display: block; font-size: 40px; letter-spacing: 1px; white-space: nowrap; }
  .brand__sub { display: block; font-size: 14px; letter-spacing: 3px; white-space: nowrap; }

  .card--front .brand { position: absolute; top: 48px; right: 34px; }

  .contact { position: absolute; left: 40px; top: 176px; color: var(--ink); }
  .contact__name {
    font-weight: 700; font-size: 17px; letter-spacing: 1px;
    text-transform: uppercase; margin-bottom: 10px;
  }
  .contact__line {
    display: flex; align-items: center; gap: 6px;
    font-size: 14px; line-height: 20px; white-space: nowrap;
  }
  .contact__line--place { margin-top: 8px; }
  .icon { width: 12px; height: 12px; fill: var(--ink); flex: none; }

  .card--back .brand {
    position: absolute; left: 0; right: 0; top: 92px; color: var(--silver);
  }
  .tagline {
    position: absolute; left: 0; right: 0; top: 196px;
    text-align: center; font-size: 11px; letter-spacing: 1.5px;
    text-transform: uppercase; color: var(--muted);
  }
</style>
</head>
<body>
  <section class="card card--front" aria-label="Card front">
    <div class="brand">
      <span class="brand__name">Miss Poppy's</span>
      <span class="brand__sub">Soak Parlour</span>
    </div>
    <div class="contact">
      <p class="contact__name">Donna Pickett</p>
      <p class="contact__line">
        <svg class="icon" viewBox="0 0 24 24" aria-hidden="true"><path d="M6.6 10.8a15 15 0 0 0 6.6 6.6l2.2-2.2a1 1 0 0 1 1-.25 11.4 11.4 0 0 0 3.6.57 1 1 0 0 1 1 1V20a1 1 0 0 1-1 1A17 17 0 0 1 3 4a1 1 0 0 1 1-1h3.5a1 1 0 0 1 1 1c0 1.25.2 2.45.57 3.57a1 1 0 0 1-.25 1z"/></svg>
        1.702.555.0143
      </p>
      <p class="contact__line">
        <svg class="icon" viewBox="0 0 24 24" aria-hidden="true"><path d="M2 5h20v14H2zm2 2v.5l8 5 8-5V7zm0 2.8V17h16V9.8l-8 5z"/></svg>
        dpickett47@mailpost.example
      </p>
      <p class="contact__line contact__line--place">
        <svg class="icon" viewBox="0 0 24 24" aria-hidden="true"><path d="M12 2a7 7 0 0 0-7 7c0 5 7 13 7 13s7-8 7-13a7 7 0 0 0-7-7zm0 9.5A2.5 2.5 0 1 1 12 6.5a2.5 2.5 0 0 1 0 5z"/></svg>
        Silver Hollow Nevada
      </p>
    </div>
  </section>

  <section class="card card--back" aria-label="Card back">
    <div class="brand">
      <span class="brand__name">Miss Poppy's</span>
      <span class="brand__sub">Soak Parlour</span>
    </div>
    <p class="tagline">Maker of bath bombs, bath salts &amp; more..</p>
  </section>
</body>
</html>
```